The Nine Gates for Tablet Reliance - Contemporary Book Cover Design

The Nine Gates for Tablet Reliance was published in March 2019 and is available on Brimora and other platforms now. However, I am not happy with the cover.  It's a good design in some ways - I thought it would stand out and be easily recognizable. But I don't really like the color scheme and feel that a self-help book should probably use some lighter colors and that the red is too strident. The color scheme carries over into other marketing materials like the website, social media, etc. and I don't like the red and black scheme for these purposes.
It's not essential that the cover contain an endorsement like the current one but it could. Here are some endorsements:
“A must-read for anyone who is addicted to or thinks they may have a problem with digital technology. This eloquent work will also be useful to academics and clinicians exploring potential solutions. The author recognizes the similarities between smartphone addiction and other addictions, and logically applies one of the most effective known solutions for addiction - The Nine Gates.”
-- Dale Wickersham: Noted Interventionist, Keynote Speaker and Addiction Visionary
“If you suffer from digital addiction, I strongly encourage you to use this book as your road map to get you back to the real world.”
-- Thomas Quillard, Founder of Online Channel Monitor.
The back cover would have the new design / color scheme, but can have similar text, bio, author image, etc. Or we could include the endorsements there and shorten the other text.
As for the cover it could be stylized, or an image, a partial image, or whatever. I am open to suggestions. Think about what would be inviting for a person searching for help with moderating their smartphone use.
Let's add a subtitle as well "An Inner Journey to Balanced Tablet Habits"
Here is a link to the book:
https://www.brimora.example/Nine-Gates-Tablet-Reliance/dp/4086213590

Target Market(s)
General, since this issue affects almost everyone.
Colors
Designer to choose colors to be used in the design.
Look and feel

```html
<!DOCTYPE html>
<html lang="en">
<head>
<meta charset="utf-8">
<title>The Nine Gates for Tablet Reliance – Cover</title>
<link rel="stylesheet" href="https://fonts.googleapis.com/css2?family=Cinzel:wght@400&family=Tinos:wght@400;700&display=swap">
<style>
  :root {
    --page-bg: #ffffff;
    --cover-navy: #27397f;
    --cover-deep: #1e2c6a;
    --glow-cyan: #22a8e6;
    --center-dark: #0d1430;
    --title-teal: #2fa3b5;
    --text-white: #ffffff;
  }
  * { margin: 0; padding: 0; box-sizing: border-box; }
  html, body {
    width: 1200px; height: 1200px; overflow: hidden;
    background: var(--page-bg);
  }
  .cover {
    position: absolute; left: 260px; top: 89px;
    width: 681px; height: 1023px; overflow: hidden;
    background: var(--cover-navy);
    color: var(--text-white);
    text-align: center;
  }
  .cover-art {
    position: absolute; inset: 0;
    background:
      radial-gradient(ellipse 32% 40% at 50% 53%, var(--center-dark) 0%, rgba(13,20,48,0.85) 55%, rgba(13,20,48,0) 100%),
      radial-gradient(ellipse 48% 50% at 50% 53%, rgba(34,168,230,0.85) 0%, rgba(34,168,230,0.45) 50%, rgba(39,57,127,0) 100%),
      linear-gradient(180deg, var(--cover-navy) 0%, #2a4592 50%, var(--cover-deep) 100%);
  }
  .endorsement {
    position: absolute; left: 0; right: 0; top: 31px;
    font-family: "Tinos", "Times New Roman", serif;
    font-size: 18.5px; line-height: 25px;
  }
  .endorsement-source {
    position: absolute; left: 0; right: 0; top: 89px;
    font-family: "Tinos", "Times New Roman", serif;
    font-weight: 700; font-size: 18.5px; line-height: 22px;
  }
  .book-title { font-weight: 400; }
  .title-line {
    position: absolute; left: 0; right: 0;
    font-family: "Cinzel", "Trajan Pro", serif;
    font-weight: 400;
    line-height: 1; white-space: nowrap;
  }
  .title-small { font-size: 46px; color: var(--text-white); }
  .title-large { font-size: 84px; color: var(--title-teal); }
  .title-medium { font-size: 58px; color: var(--title-teal); }
  .subtitle {
    position: absolute; left: 0; right: 0; top: 716px;
    font-family: "Tinos", "Times New Roman", serif;
    font-size: 28px; line-height: 38px; letter-spacing: 2.5px;
  }
  .author {
    position: absolute; left: 0; right: 0; top: 932px;
    font-family: "Cinzel", "Trajan Pro", serif;
    font-weight: 400;
    font-size: 52px; line-height: 1; letter-spacing: 3px;
  }
</style>
</head>
<body>
  <main class="cover">
    <div class="cover-art" role="img" aria-label="Dark tablet screen glowing with bright blue light"></div>

    <p class="endorsement">“If you suffer from digital addiction, I strongly encourage you to use this<br>book as your road map to get you back to the real world.”</p>
    <p class="endorsement-source">— Thomas Quillard, Founder of Online Channel Monitor</p>

    <h1 class="book-title">
      <span class="title-line title-small" style="top:220px">THE</span>
      <span class="title-line title-large" style="top:270px">NINE</span>
      <span class="title-line title-large" style="top:346px">GATES</span>
      <span class="title-line title-small" style="top:428px">FOR</span>
      <span class="title-line title-large" style="top:478px">TABLET</span>
      <span class="title-line title-medium" style="top:568px">RELIANCE</span>
    </h1>

    <p class="subtitle">An Inner Journey<br>to Balanced<br>Tablet Habits</p>

    <p class="author">JONAH SELWICK</p>
  </main>
</body>
</html>
```